Lose Up To 1 LB Of Fat Per Day

We need a double sided street sign for our weight loss clinic. We need the doctors picture to the right side of the sign and we need a challenge “Lose Up To 1 Pound Of Fat Per Day” included in the signage.
Our color scheme for the clinic are black, white, teal and silver.
The phone number should be at the bottom of the sign
555-206–3948

Target Market(s)

Weight Loss

Font styles to use
Sans Serif

```html
<!DOCTYPE html>
<html lang="en">
<head>
<meta charset="utf-8">
<title>Weight Loss Clinic Street Sign</title>
<link rel="stylesheet" href="https://fonts.googleapis.com/css2?family=Montserrat:ital,wght@0,700;0,800;1,400;1,700;1,800&display=swap">
<style>
  :root {
    --page-bg: #eceeef;
    --sign-bg: #d5dee7;
    --teal: #0e8079;
    --silver-light: #f4f4f4;
    --silver-dark: #9a9a9a;
    --ink: #111111;
    --photo-light: #e3e9ee;
    --photo-coat: #f5f7f9;
  }
  html, body {
    margin: 0;
    width: 1200px;
    height: 1200px;
    overflow: hidden;
    background: var(--page-bg);
    font-family: "Montserrat", Arial, sans-serif;
  }
  .sign {
    position: absolute;
    left: 83px;
    top: 341px;
    width: 1034px;
    height: 518px;
    background: var(--sign-bg);
    overflow: hidden;
  }
  .sign-graphics {
    position: absolute;
    inset: 0;
    width: 100%;
    height: 100%;
  }
  .doctor-photo {
    position: absolute;
    left: 680px;
    top: 40px;
    width: 300px;
    height: 478px;
    border-radius: 140px 140px 0 0;
    background: linear-gradient(180deg, var(--photo-light) 0%, var(--photo-coat) 45%, #e9eef2 100%);
  }
  .headline { position: absolute; left: 76px; margin: 0; color: var(--ink); line-height: 1; white-space: nowrap; }
  .headline-lead { top: 130px; font-size: 30px; font-style: italic; font-weight: 400; }
  .headline-claim { top: 164px; font-size: 50px; font-style: italic; font-weight: 800; color: var(--teal); letter-spacing: -0.5px; }
  .headline-tail { top: 221px; font-size: 44px; font-style: italic; font-weight: 400; }
  .phone {
    position: absolute;
    left: 76px;
    top: 418px;
    display: flex;
    align-items: center;
    gap: 18px;
    font-size: 41px;
    font-weight: 800;
    color: var(--ink);
    line-height: 1;
  }
  .phone-icon { width: 34px; height: 34px; }
</style>
</head>
<body>
  <div class="sign">
    <div class="doctor-photo" role="img" aria-label="Smiling doctor in white coat with stethoscope, pointing toward the headline"></div>

    <svg class="sign-graphics" viewBox="0 0 827 414" preserveAspectRatio="none" aria-hidden="true">
      <defs>
        <linearGradient id="silver" x1="0" y1="0" x2="1" y2="0">
          <stop offset="0" stop-color="var(--silver-dark)"/>
          <stop offset="0.35" stop-color="var(--silver-light)"/>
          <stop offset="0.7" stop-color="var(--silver-dark)"/>
          <stop offset="1" stop-color="var(--silver-light)"/>
        </linearGradient>
      </defs>
      <path class="swoosh-top-silver" fill="url(#silver)" d="M0,26 C320,28 470,150 518,285 C462,165 320,40 0,38 Z"/>
      <path class="swoosh-top" fill="var(--teal)" d="M0,0 L270,0 C420,30 510,150 518,285 C470,150 320,30 0,28 Z"/>
      <path class="swoosh-bottom-silver" fill="url(#silver)" d="M0,312 C110,310 200,288 250,225 C212,300 110,324 0,324 Z"/>
      <path class="swoosh-bottom" fill="var(--teal)" d="M0,292 C110,290 210,270 250,225 C200,290 110,312 0,314 Z"/>
    </svg>

    <p class="headline headline-lead">Lose Up To</p>
    <p class="headline headline-claim">1 Pound of Fat</p>
    <p class="headline headline-tail">Per Day</p>

    <div class="phone">
      <svg class="phone-icon" viewBox="0 0 24 24" aria-hidden="true">
        <circle cx="12" cy="12" r="10.5" fill="none" stroke="var(--ink)" stroke-width="1.8"/>
        <path fill="var(--ink)" d="M8.3 6.6c.4-.3.9-.2 1.1.2l1.1 1.9c.2.4.1.8-.2 1.1l-.7.6c.5 1.3 1.5 2.4 2.9 3l.6-.7c.3-.3.8-.4 1.1-.2l1.9 1.1c.4.2.5.8.2 1.1l-.9 1c-.5.5-1.2.7-1.9.5-3-1-5.2-3.2-6.2-6.2-.2-.7 0-1.4.5-1.9z"/>
      </svg>
      <span class="phone-number">555-206–3948</span>
    </div>
  </div>
</body>
</html>
```